Verbena Home- Hang tags for Modern Handmade Home Decor products

We need to design some hang tags to use for our products, we want double tags, meaning two tags that go together on one string, two different and coordinating sizes and shapes. We have a logo, what we need is the artwork for these two tags to take to print. One tag will have the logo on one side and company information on the other, the second tag will be for product information. For example, we specialize in handmade pieces from Latin America, on the product tag I want space to write the product info but also a line for what country it's from and what community created it. I'm attaching an image of the shapes of tags that I like, along with a copy of our logo. On the larger company tag I'd like our logo in the center and a color block stripe of the yellow color of our logo at the bottom, on the flip side there will just be text, sort of our company motto. On the narrower longer product info tag I'd like a small logo at the bottom end and space for product information to be written in by hand and on the flip side of this one lines for what country it's from, what community created it and care instructions, again, all information that we will write in by hand. Please let me know if you have questions.

Target Market(s)

Design savvy, house proud, well educated people who travel and appreciate art.

Font styles to use
Sans Serif

Requirements
Must have
• I want it to look graphic, sophisticated and modern. I want to be very legible and clean.
Nice to have
• Clarity, easy to read, and maybe a bit of whimsy or lightheartedness.
Should not have
• Nothing that feels "ethnic" or "crafty:, even though our products are handmade in Latin America they are contemporary and sophisticated, not stereotypical.

```html
<!DOCTYPE html>
<html lang="en">
<head>
<meta charset="utf-8">
<title>Verbena Home – Hang Tags</title>
<link href="https://fonts.googleapis.com/css2?family=Questrial&display=swap" rel="stylesheet">
<style>
  :root {
    --backdrop: #eeeeec;
    --kraft: #b88f63;
    --kraft-edge: #a98158;
    --sun-yellow: #f6c71e;
    --ink-white: #ffffff;
    --reinforce-grey: #c9c9c7;
    --hole: #6f5538;
  }
  * { box-sizing: border-box; margin: 0; padding: 0; }
  html, body {
    width: 1200px;
    height: 894px;
    overflow: hidden;
    background: var(--backdrop);
  }
  .canvas {
    position: relative;
    width: 1200px;
    height: 894px;
    font-family: "Questrial", "Helvetica Neue", Arial, sans-serif;
    color: var(--ink-white);
  }

  /* ---------- Narrow product tag (shared) ---------- */
  .product-tag {
    position: absolute;
    width: 278px;
    height: 798px;
    background: var(--kraft);
    border-radius: 16px;
    box-shadow: 0 2px 6px rgba(0,0,0,0.18);
  }
  .punch-hole {
    position: absolute;
    border-radius: 50%;
    background: var(--hole);
  }
  .product-tag .punch-hole {
    width: 15px; height: 15px;
    left: 121px; top: 70px;
  }

  /* Back side: hand-write lines */
  .product-tag--back {
    left: 188px;
    top: -7px;
    transform: rotate(30deg);
  }
  .info-lines {
    position: absolute;
    width: 798px;
    height: 278px;
    left: -260px;
    top: 260px;
    transform: rotate(-90deg);
    padding: 72px 0 0 54px;
  }
  .info-row {
    display: flex;
    align-items: flex-end;
    height: 45px;
    font-size: 23px;
    letter-spacing: 2.5px;
  }
  .info-row__label { white-space: nowrap; padding-right: 4px; }
  .info-row__rule {
    height: 2px;
    background: var(--ink-white);
    margin-bottom: 5px;
  }
  .info-row:nth-child(1) .info-row__rule { width: 430px; }
  .info-row:nth-child(2) .info-row__rule { width: 400px; }
  .info-row:nth-child(3) .info-row__rule { width: 270px; }
  .info-row:nth-child(4) .info-row__rule { width: 560px; margin-left: 0; }

  /* Front side: small wordmark */
  .product-tag--front {
    left: 363px;
    top: 42px;
  }
  .product-tag__brand {
    position: absolute;
    left: 0; right: 0;
    bottom: 30px;
    text-align: center;
  }

  /* ---------- Wordmark ---------- */
  .brand-dot {
    display: block;
    margin: 0 auto;
    border-radius: 50%;
    background: var(--sun-yellow);
  }
  .brand-name {
    display: block;
    font-weight: 400;
    letter-spacing: 0.5px;
    line-height: 1;
  }
  .brand-url {
    display: block;
    letter-spacing: 2.4px;
  }
  .product-tag__brand .brand-dot { width: 56px; height: 56px; margin-bottom: 26px; }
  .product-tag__brand .brand-name { font-size: 34px; }
  .product-tag__brand .brand-url { font-size: 8.5px; margin-top: 8px; }

  /* ---------- Company tag ---------- */
  .company-tag {
    position: absolute;
    left: 669px;
    top: 195px;
    width: 339px;
    height: 527px;
    background: var(--kraft);
    clip-path: polygon(49px 0, 290px 0, 339px 78px, 339px 527px, 0 527px, 0 78px);
  }
  .company-tag__reinforcement {
    position: absolute;
    left: 89px;
    top: 0;
    width: 160px;
    height: 81px;
    background: var(--reinforce-grey);
  }
  .company-tag .punch-hole {
    width: 31px; height: 31px;
    left: 154px; top: 30px;
    background: #e6e6e4;
    box-shadow: inset 0 1px 3px rgba(0,0,0,0.35);
  }
  .company-tag__brand {
    position: absolute;
    left: 0; right: 0;
    top: 180px;
    text-align: center;
  }
  .company-tag__brand .brand-dot { width: 120px; height: 120px; margin-bottom: 40px; }
  .company-tag__brand .brand-name { font-size: 58px; }
  .company-tag__brand .brand-url { font-size: 11.5px; margin-top: 12px; }
  .company-tag__stripe {
    position: absolute;
    left: 0; right: 0;
    bottom: 0;
    height: 53px;
    background: var(--sun-yellow);
  }
</style>
</head>
<body>
<main class="canvas">

  <!-- Product tag, handwriting side -->
  <section class="product-tag product-tag--back" aria-label="Product tag, reverse">
    <span class="punch-hole"></span>
    <div class="info-lines">
      <div class="info-row"><span class="info-row__label">Origin</span><span class="info-row__rule"></span></div>
      <div class="info-row"><span class="info-row__label">Community</span><span class="info-row__rule"></span></div>
      <div class="info-row"><span class="info-row__label">Care Instructions</span><span class="info-row__rule"></span></div>
      <div class="info-row"><span class="info-row__rule"></span></div>
    </div>
  </section>

  <!-- Product tag, brand side -->
  <section class="product-tag product-tag--front" aria-label="Product tag, front">
    <span class="punch-hole"></span>
    <div class="product-tag__brand">
      <span class="brand-dot"></span>
      <span class="brand-name">verbena</span>
      <span class="brand-url">www.verbenahome.com</span>
    </div>
  </section>

  <!-- Company tag -->
  <section class="company-tag" aria-label="Company tag, front">
    <div class="company-tag__reinforcement"></div>
    <span class="punch-hole"></span>
    <div class="company-tag__brand">
      <span class="brand-dot"></span>
      <span class="brand-name">verbena</span>
      <span class="brand-url">www.verbenahome.com</span>
    </div>
    <div class="company-tag__stripe"></div>
  </section>

</main>
</body>
</html>
```